Velmora Handel Stationary
Simple
Jonas Brückler
Co-Founder
Velmora Handel UG
Lindenkamp 12
48213 Kestrelheim
Germany
jonas.brueckler@velmora-handel.example
www.velmora-handel.example
Please use the some font as in the logo and work out a proposal based on the red and yellow logo in the uploaded rar file. Whether or not you use the globe in the back (you will see in the rar file) is up to you. The corporate slogan 'Your gateway to infinite opportunities' can be integrated but it's not a must.
Corporate Logo (with or without slogan, up to you)
Please refer to the logos. Ideally work sth out from the colorful version (red and yellow) with or without the globe in the back. You will see when looking at the file.

```html
<!DOCTYPE html>
<html lang="de">
<head>
<meta charset="utf-8">
<title>Velmora Handel – Visitenkarten</title>
<link rel="stylesheet" href="https://fonts.googleapis.com/css2?family=Libre+Baskerville&family=Oswald:wght@700&family=Open+Sans:wght@400;600;700&display=swap">
<style>
  :root {
    --page: #ffffff;
    --label: #8a8a8a;
    --brand-red: #d8141c;
    --brand-orange: #f2a200;
    --text: #444444;
    --muted: #777777;
    --rule: #d8141c;
    --card-edge: #e4e4e4;
    --grey-a: #f4f4f4;
    --grey-b: #b9b9b9;
    --yellow-a: #ffd21a;
    --yellow-b: #f29100;
    --wine-a: #c2202c;
    --wine-b: #5a0c14;
  }
  html, body {
    margin: 0;
    width: 1200px;
    height: 593px;
    overflow: hidden;
    background: var(--page);
  }
  .sheet {
    position: relative;
    width: 1200px;
    height: 593px;
  }
  .side-label {
    position: absolute;
    width: 350px;
    text-align: center;
    font-family: "Libre Baskerville", serif;
    font-weight: 400;
    font-size: 22px;
    letter-spacing: 1px;
    color: var(--label);
    margin: 0;
  }
  .card {
    position: absolute;
    width: 350px;
    height: 208px;
    box-shadow: 0 6px 10px rgba(0,0,0,0.22);
    overflow: hidden;
  }
  .card--front,
  .card--white { background: #ffffff; border: 1px solid var(--card-edge); box-sizing: border-box; }
  .card--grey { background: radial-gradient(circle at 50% 50%, var(--grey-a) 0%, var(--grey-b) 100%); }
  .card--yellow { background: radial-gradient(circle at 50% 55%, var(--yellow-a) 0%, var(--yellow-b) 100%); }
  .card--wine { background: radial-gradient(circle at 50% 50%, var(--wine-a) 0%, var(--wine-b) 100%); }

  .brand {
    position: absolute;
    left: 14px;
    top: 68px;
    width: 140px;
    text-align: center;
  }
  .brand__dot {
    display: block;
    width: 34px;
    height: 34px;
    margin: 0 auto 6px;
    border-radius: 50%;
    background: var(--brand-red);
  }
  .brand__name {
    font-family: "Oswald", sans-serif;
    font-weight: 700;
    font-size: 20px;
    line-height: 1.05;
    color: var(--brand-red);
    letter-spacing: 0.5px;
  }
  .divider {
    position: absolute;
    left: 165px;
    top: 58px;
    width: 2px;
    height: 92px;
    background: var(--rule);
  }
  .contact {
    position: absolute;
    left: 176px;
    top: 56px;
    width: 165px;
    font-family: "Open Sans", sans-serif;
    color: var(--text);
  }
  .contact__name {
    margin: 0;
    font-size: 11px;
    font-weight: 700;
    color: var(--brand-red);
  }
  .contact__role {
    margin: 0 0 8px;
    font-size: 7px;
    color: var(--muted);
  }
  .contact__address {
    margin: 0 0 5px;
    font-style: normal;
    font-size: 6.5px;
    line-height: 1.4;
  }
  .contact__lines {
    list-style: none;
    margin: 0;
    padding: 0;
    font-size: 6.5px;
    line-height: 1.55;
  }
  .contact__lines li { display: flex; align-items: center; gap: 4px; white-space: nowrap; }
  .icon { width: 7px; height: 7px; fill: var(--brand-red); flex: none; }

  .back-mark {
    position: absolute;
    left: 0; right: 0;
    top: 80px;
    text-align: center;
  }
  .back-mark__dot {
    display: block;
    width: 36px;
    height: 36px;
    margin: 0 auto 6px;
    border-radius: 50%;
    background: var(--brand-red);
  }
  .back-mark__name {
    font-family: "Oswald", sans-serif;
    font-weight: 700;
    font-size: 11px;
    letter-spacing: 1px;
    color: var(--brand-red);
  }
  .card--wine .back-mark__dot { background: var(--brand-orange); }
  .card--wine .back-mark__name { color: var(--brand-orange); }
</style>
</head>
<body>
<main class="sheet">
  <h2 class="side-label" style="left:40px;top:28px">FRONT</h2>
  <h2 class="side-label" style="left:425px;top:28px">BACK</h2>
  <h2 class="side-label" style="left:810px;top:28px">BACK</h2>

  <section class="card card--front" style="left:40px;top:62px">
    <div class="brand">
      <span class="brand__dot"></span>
      <div class="brand__name">VELMORA<br>HANDEL</div>
    </div>
    <div class="divider"></div>
    <div class="contact">
      <p class="contact__name">Jonas Brückler</p>
      <p class="contact__role">Co-Founder</p>
      <address class="contact__address">Velmora Handel UG, Lindenkamp 12<br>48213 Kestrelheim, Germany</address>
      <ul class="contact__lines">
        <li><svg class="icon" viewBox="0 0 10 10"><path d="M2 0h2l1 3-1.5 1a6 6 0 0 0 2.5 2.5L7 5l3 1v2a2 2 0 0 1-2 2A8 8 0 0 1 0 2a2 2 0 0 1 2-2z"/></svg>+49 555 0142 20</li>
        <li><svg class="icon" viewBox="0 0 10 10"><rect x="2.5" y="0" width="5" height="10" rx="1"/></svg>+49 155 5014 6613</li>
        <li><svg class="icon" viewBox="0 0 10 10"><path d="M0 2h10v6H0z M0 2l5 3.5L10 2"/></svg>jonas.brueckler@velmora-handel.example</li>
        <li><svg class="icon" viewBox="0 0 10 10"><circle cx="5" cy="5" r="5"/></svg>www.velmora-handel.example</li>
      </ul>
    </div>
  </section>

  <section class="card card--grey" style="left:425px;top:62px">
    <div class="back-mark"><span class="back-mark__dot"></span><span class="back-mark__name">VELMORA HANDEL</span></div>
  </section>

  <section class="card card--white" style="left:810px;top:62px">
    <div class="back-mark"><span class="back-mark__dot"></span><span class="back-mark__name">VELMORA HANDEL</span></div>
  </section>

  <h2 class="side-label" style="left:40px;top:303px">FRONT</h2>
  <h2 class="side-label" style="left:425px;top:303px">BACK</h2>
  <h2 class="side-label" style="left:810px;top:303px">BACK</h2>

  <section class="card card--front" style="left:40px;top:337px">
    <div class="brand">
      <span class="brand__dot"></span>
      <div class="brand__name">VELMORA<br>HANDEL</div>
    </div>
    <div class="divider"></div>
    <div class="contact">
      <p class="contact__name">Jonas Brückler</p>
      <p class="contact__role">Co-Founder</p>
      <address class="contact__address">Velmora Handel UG, Lindenkamp 12<br>48213 Kestrelheim, Germany</address>
      <ul class="contact__lines">
        <li><svg class="icon" viewBox="0 0 10 10"><path d="M2 0h2l1 3-1.5 1a6 6 0 0 0 2.5 2.5L7 5l3 1v2a2 2 0 0 1-2 2A8 8 0 0 1 0 2a2 2 0 0 1 2-2z"/></svg>+49 555 0142 20</li>
        <li><svg class="icon" viewBox="0 0 10 10"><rect x="2.5" y="0" width="5" height="10" rx="1"/></svg>+49 155 5014 6613</li>
        <li><svg class="icon" viewBox="0 0 10 10"><path d="M0 2h10v6H0z M0 2l5 3.5L10 2"/></svg>jonas.brueckler@velmora-handel.example</li>
        <li><svg class="icon" viewBox="0 0 10 10"><circle cx="5" cy="5" r="5"/></svg>www.velmora-handel.example</li>
      </ul>
    </div>
  </section>

  <section class="card card--yellow" style="left:425px;top:337px">
    <div class="back-mark"><span class="back-mark__dot"></span><span class="back-mark__name">VELMORA HANDEL</span></div>
  </section>

  <section class="card card--wine" style="left:810px;top:337px">
    <div class="back-mark"><span class="back-mark__dot"></span><span class="back-mark__name">VELMORA HANDEL</span></div>
  </section>
</main>
</body>
</html>
```